high end contractor

high end contracting company we do all phases of construction kitchen,bathrooms,etc... please look at my website before you design www.harborlinebld.com

would love some sort of lines or logo or both

Industry/Entity Type

Construction

Contact Information for Business Card

company name: harbor & lantern contracting address: 412 birchwood ave mount Vernon ny 10552 email: harborlinebld@mailzone.com website: www.harborlinebld.com office#: 914-555-0182 fax#: 914-555-0197 dominic fersalo mobile# 917-555-0263

```html
<!DOCTYPE html>
<html lang="en">
<head>
<meta charset="utf-8">
<title>Harbor &amp; Lantern Renovations – Business Card</title>
<link rel="stylesheet" href="https://fonts.googleapis.com/css2?family=Signika:wght@400;600&family=Arimo:ital@1&display=swap">
<style>
  :root {
    --page: #ffffff;
    --card: #1b1b1b;
    --teal: #4cbcbc;
    --teal-mid: #3f9c9a;
    --teal-soft: #45aaa8;
    --teal-dark: #3c6f6b;
    --teal-deep: #48645f;
    --white: #f2f2f2;
    --icon: #d9d9d9;
  }
  * { margin: 0; padding: 0; box-sizing: border-box; }
  html, body { width: 1200px; height: 1000px; overflow: hidden; background: var(--page); }
  .canvas { position: relative; width: 1200px; height: 1000px; }

  .card {
    position: absolute;
    width: 640px;
    height: 340px;
    background: var(--card);
    border-radius: 26px;
    overflow: hidden;
  }
  .card--contact { left: 88px; top: 118px; }
  .card--showcase { left: 426px; top: 440px; height: 336px; }

  .wordmark {
    position: absolute;
    font-family: "Signika", sans-serif;
    font-size: 23px;
    line-height: 26px;
    letter-spacing: 0.6px;
    white-space: nowrap;
  }
  .wordmark__name { color: var(--teal); font-weight: 600; }
  .wordmark__trade { color: var(--white); font-weight: 400; }
  .card--contact .wordmark { left: 90px; top: 37px; }
  .card--showcase .wordmark { left: 83px; top: 35px; }

  .stripes { position: absolute; top: 0; right: 0; height: 100%; width: 101px; display: flex; }
  .stripes span { height: 100%; }
  .stripe--dark { width: 10px; background: var(--teal-dark); }
  .stripe--mid { width: 14px; background: var(--teal-mid); }
  .stripe--soft { width: 9px; background: var(--teal-soft); }
  .stripe--bright { width: 41px; background: var(--teal); }
  .stripe--mid-r { width: 13px; background: var(--teal-mid); }
  .stripe--deep { width: 14px; background: var(--teal-deep); }

  .contact {
    position: absolute;
    font-family: "Arimo", sans-serif;
    font-style: italic;
    font-size: 17px;
    color: var(--teal);
    white-space: nowrap;
    line-height: 22px;
  }
  .contact svg { position: absolute; fill: none; stroke: var(--icon); stroke-width: 1.3; }
  .contact--address { left: 58px; top: 195px; }
  .contact--address .contact__text { padding-left: 26px; }
  .contact--address .contact__text span { display: block; }
  .contact--address .contact__text span + span { margin-left: -4px; }
  .contact--email { left: 47px; top: 246px; }
  .contact--email .contact__text { padding-left: 24px; }
  .phones { position: absolute; left: 42px; top: 285px; }
  .phone { position: absolute; top: 0; }
  .phone--office { left: 0; }
  .phone--fax { left: 158px; }
  .phone--mobile { left: 317px; }
  .phone .contact__text { padding-left: 21px; }
  .phone--mobile .contact__text { padding-left: 17px; }

  .speed-lines { position: absolute; left: 72px; top: 243px; width: 268px; height: 14px; }
  .speed-lines span {
    position: absolute; height: 3px;
    background: linear-gradient(90deg, rgba(76,188,188,0) 0%, var(--teal) 22%, var(--teal) 100%);
  }
  .speed-lines span:first-child { top: 0; left: 22px; width: 246px; }
  .speed-lines span:last-child { top: 9px; left: 0; width: 268px; }

  .project-photo { position: absolute; border-radius: 50%; border: 4px solid var(--card); }
  .project-photo--kitchen { left: 474px; top: 43px; width: 124px; height: 124px;
    background: linear-gradient(180deg, #e4e4e4 0%, #9a9a98 55%, #6d6d6d 100%); }
  .project-photo--living { left: 438px; top: 142px; width: 160px; height: 160px;
    background: linear-gradient(160deg, #dcdcdc 0%, #b5b3ae 50%, #4a4a4a 100%); }
  .project-photo--bath { left: 342px; top: 184px; width: 128px; height: 128px;
    background: linear-gradient(180deg, #5a6872 0%, #9aa4aa 45%, #e6e6e6 100%); }
</style>
</head>
<body>
<main class="canvas">

  <section class="card card--contact" aria-label="Business card, contact side">
    <h1 class="wordmark"><span class="wordmark__name">HARBOR &amp; LANTERN</span> <span class="wordmark__trade">RENOVATIONS</span></h1>

    <div class="contact contact--address">
      <svg width="16" height="16" viewBox="0 0 16 16" style="left:0;top:3px" aria-hidden="true">
        <path d="M1.5 8 L8 2 L14.5 8 M3.5 6.5 V14 H12.5 V6.5 M6.5 14 V10 H9.5 V14"/>
      </svg>
      <p class="contact__text"><span>412 Birchwood Avenue</span><span>Lanterndale, NY 10599</span></p>
    </div>

    <div class="contact contact--email">
      <svg width="16" height="14" viewBox="0 0 16 14" style="left:0;top:4px" aria-hidden="true">
        <path d="M1 5 L8 1 L15 5 V13 H1 Z M1 5 L8 9.5 L15 5"/>
      </svg>
      <p class="contact__text">email: harborlinebld@mailzone.com</p>
    </div>

    <div class="phones contact">
      <div class="phone phone--office">
        <svg width="12" height="14" viewBox="0 0 12 14" style="left:0;top:4px;fill:var(--icon);stroke:none" aria-hidden="true">
          <path d="M2 1 L5 1 L5.5 4 L3.8 5 C4.5 7.5 5.5 9 7.5 10.3 L8.8 8.8 L11 10 L11 13 C5.5 13 1 8 2 1 Z"/>
        </svg>
        <p class="contact__text">914-555-0182</p>
      </div>
      <div class="phone phone--fax">
        <svg width="14" height="12" viewBox="0 0 14 12" style="left:0;top:5px;fill:var(--icon);stroke:none" aria-hidden="true">
          <rect x="3" y="0" width="8" height="4"/><rect x="0" y="4" width="14" height="6" rx="1"/><rect x="3" y="8" width="8" height="4" fill="#1b1b1b" stroke="#d9d9d9"/>
        </svg>
        <p class="contact__text">914-555-0197</p>
      </div>
      <div class="phone phone--mobile">
        <svg width="10" height="16" viewBox="0 0 10 16" style="left:0;top:3px" aria-hidden="true">
          <rect x="1" y="1" width="8" height="14" rx="1.5"/><rect x="3" y="3" width="4" height="4"/>
        </svg>
        <p class="contact__text">917-555-0263</p>
      </div>
    </div>

    <div class="stripes" aria-hidden="true">
      <span class="stripe--dark"></span><span class="stripe--mid"></span><span class="stripe--soft"></span><span class="stripe--bright"></span><span class="stripe--mid-r"></span><span class="stripe--deep"></span>
    </div>
  </section>

  <section class="card card--showcase" aria-label="Business card, showcase side">
    <h2 class="wordmark"><span class="wordmark__name">HARBOR &amp; LANTERN</span> <span class="wordmark__trade">RENOVATIONS</span></h2>

    <div class="speed-lines" aria-hidden="true"><span></span><span></span></div>

    <div class="project-photo project-photo--kitchen" role="img" aria-label="Photo of a renovated modern kitchen with white cabinets"></div>
    <div class="project-photo project-photo--living" role="img" aria-label="Photo of a renovated living room with dark leather sofa"></div>
    <div class="project-photo project-photo--bath" role="img" aria-label="Photo of a renovated bathroom with mosaic tile and white sink"></div>
  </section>

</main>
</body>
</html>
```